Brochure for a civil enineering company in A4 format

I need a brochure design for our company VELTA Engineering S.r.l.. We are an engineering consultant company. Our main clients are from the infrastructure industry (geotechnical and underground sectors mainly).
We are looking for a 2 pages (4 faces) fold out design with a glued pocket where we can put individual data sheets.
I need A4 format pages.

Target Market(s)

We are an engineering consultant company. Our main clients are from the infrastructure industry (geotechnical and underground sectors mainly).

Industry/Entity Type

Civil Engineer

Font styles to use
Sans Serif

Requirements
Must have
• Overall: 2 pages in A4 format
Essential style. Bright and modern appearance.
Glued pocket
Logo integrated in a picture on the pocket where I would like to insert a slogan (… velta engineering … reliable solutions …)
Attached are selected images which the designer can use and edit at their own discretion.
Some advice in the following (anyway designers are free to provide their solutions):
Outer sheets:
Front page with name, logo. It could be nice to have the “m” of the logo integrated in a pictures, also a modified picture (I mean modify one of the attached pictures) so to create a general image and do not tie the cover to a specific job.
Back page: offices address and contact email address. Nice to have one space for a slogan.
Inner sheet: text that I upload in the file “inside-sheets”, possibly with pictures on each sheet. In the right faces insert the glued pocket. On this pages insert the section OUR EXPERIENCE ….with a space for a picture of our team.
Nice to have
• Clean and essential design.
Pictures choosing from the atteched ones. Pictures could be modified in a very light manner to make them a general idea of the work ( I mean geotechnical world) without to be immediately linked to a specific site.
Should not have
• excessive frills

```html
<!DOCTYPE html>
<html lang="en">
<head>
<meta charset="utf-8">
<title>VELTA Engineering – Folder</title>
<link href="https://fonts.googleapis.com/css2?family=Lato:wght@400;700;900&display=swap" rel="stylesheet">
<style>
  :root{
    --bg:#e9e9e9;
    --black:#0d0d0f;
    --navy:#2c2f6e;
    --navy-dark:#23265c;
    --white:#ffffff;
    --grey-text:#9a9aa2;
    --photo-a:#5b6f86;
    --photo-b:#a5896a;
    --photo-c:#3b4656;
  }
  *{margin:0;padding:0;box-sizing:border-box}
  html,body{width:795px;height:1200px;overflow:hidden}
  body{background:var(--bg);font-family:"Lato",sans-serif;position:relative}

  .spread{position:absolute;left:48px;width:700px;height:495px;display:flex;box-shadow:0 2px 8px rgba(0,0,0,.18)}
  .spread--outer{top:60px;background:var(--black)}
  .spread--inner{top:640px}
  .panel{position:relative;width:350px;height:495px;overflow:hidden}

  /* back page */
  .photo-grid{position:absolute;left:22px;top:26px;display:grid;grid-template-columns:repeat(3,58px);gap:6px}
  .photo-grid .tile{width:58px;height:58px;border-radius:4px;background:linear-gradient(135deg,var(--photo-b),var(--photo-c))}
  .photo-grid .tile:nth-child(2n){background:linear-gradient(135deg,var(--photo-a),var(--photo-c))}
  .logo{display:flex;align-items:center;gap:7px;color:var(--white);font-weight:900;font-size:34px;letter-spacing:1px;text-transform:lowercase}
  .logo .dot{width:14px;height:14px;border-radius:50%;background:var(--white)}
  .back .logo{position:absolute;left:105px;top:244px}
  .contact{position:absolute;left:0;width:350px;top:305px;text-align:center;color:var(--grey-text);font-size:8px;line-height:1.7}

  /* front page */
  .front svg{position:absolute;inset:0}
  .front .logo{position:absolute;left:190px;top:212px}

  /* inner left */
  .inner-left{background:var(--navy);color:var(--white);padding:34px 26px}
  .inner-left h2{font-size:15px;font-weight:700;letter-spacing:.5px;margin-bottom:10px}
  .inner-left p{font-size:7.5px;line-height:1.65;margin-bottom:8px;color:#e1e2ef}
  .inner-left h2.services{margin-top:22px}
  .service-list{list-style:none;font-size:7.5px;line-height:1.8;color:#e1e2ef}
  .service-list li::before{content:"•";margin-right:6px}

  /* inner right */
  .inner-right{background:var(--white);color:var(--navy);padding:34px 26px}
  .inner-right h2{font-size:15px;font-weight:700;letter-spacing:.5px;margin-bottom:10px}
  .inner-right p{font-size:7.5px;line-height:1.65;margin-bottom:8px}
  .pocket{position:absolute;left:0;bottom:0;width:350px;height:220px}
  .card-slot{position:absolute;right:26px;bottom:30px;width:72px;height:42px;background:var(--white);border:1px solid #d8d8e4}
</style>
</head>
<body>

<section class="spread spread--outer">
  <div class="panel back">
    <div class="photo-grid" role="img" aria-label="Six photos of tunnel construction sites">
      <div class="tile"></div><div class="tile"></div><div class="tile"></div>
      <div class="tile"></div><div class="tile"></div><div class="tile"></div>
    </div>
    <div class="logo"><span class="dot"></span>velta</div>
    <div class="contact">
      VELTA Engineering S.r.l.<br>
      Via Roma 12, 10121 Torino, Italy<br>
      Tel +39 011 000 0000<br>
      info@veltaengineering.it<br><br>
      www.veltaengineering.it
    </div>
  </div>

  <div class="panel front">
    <svg width="350" height="495" viewBox="0 0 350 495">
      <defs>
        <linearGradient id="tunnel" x1="0" y1="0" x2="1" y2="1">
          <stop offset="0" stop-color="#8fa4bd"/>
          <stop offset=".55" stop-color="#4a5d78"/>
          <stop offset="1" stop-color="#1f2837"/>
        </linearGradient>
        <linearGradient id="site" x1="0" y1="0" x2="1" y2="1">
          <stop offset="0" stop-color="#b59774"/>
          <stop offset="1" stop-color="#3a4352"/>
        </linearGradient>
      </defs>
      <path role="img" aria-label="Photo looking through a lit tunnel under construction"
            d="M0,0 H350 V190 Q250,205 150,160 Q70,125 0,118 Z" fill="url(#tunnel)"/>
      <path d="M0,118 Q70,125 150,160 Q250,205 350,190" fill="none" stroke="#ffffff" stroke-width="3"/>
      <g role="img" aria-label="Row of tunnel and site photos set along a diagonal">
        <rect x="10" y="250" width="52" height="52" rx="6" fill="url(#site)" transform="rotate(12 36 276)"/>
        <rect x="72" y="292" width="56" height="56" rx="6" fill="url(#tunnel)" transform="rotate(12 100 320)"/>
        <rect x="140" y="335" width="60" height="60" rx="6" fill="url(#site)" transform="rotate(12 170 365)"/>
        <rect x="212" y="378" width="62" height="62" rx="6" fill="url(#tunnel)" transform="rotate(12 243 409)"/>
        <rect x="284" y="420" width="64" height="64" rx="6" fill="url(#site)" transform="rotate(12 316 452)"/>
      </g>
    </svg>
    <div class="logo"><span class="dot"></span>velta</div>
  </div>
</section>

<section class="spread spread--inner">
  <div class="panel inner-left">
    <h2>OUR COMPANY</h2>
    <p>VELTA Engineering S.r.l. is an independent consultancy providing design, analysis and site support for geotechnical and underground works. Our team combines field experience with advanced numerical methods to deliver safe and reliable solutions.</p>
    <p>We work with contractors, owners and public bodies on tunnels, shafts, slopes and deep foundations across Europe and abroad.</p>
    <h2 class="services">OUR SERVICES</h2>
    <p>From feasibility studies to construction, we follow every phase of the project with a practical approach.</p>
    <ul class="service-list">
      <li>Geotechnical design and site investigation</li>
      <li>Tunnel and shaft design by conventional and mechanised methods</li>
      <li>Numerical modelling of soil and rock</li>
      <li>Monitoring plans and data interpretation</li>
      <li>Construction support and technical assistance</li>
      <li>Back analysis and risk assessment</li>
    </ul>
  </div>

  <div class="panel inner-right">
    <h2>OUR EXPERTISE AND EXPERIENCE</h2>
    <p>Over the years our engineers have taken part in major infrastructure projects, including metro lines, railway and road tunnels, hydraulic galleries and underground stations.</p>
    <p>Each assignment is handled by a dedicated group that follows the work from the first survey to the final report, keeping close contact with the client.</p>
    <p>This experience allows us to anticipate problems and to propose efficient, safe and sustainable solutions.</p>
    <svg class="pocket" width="350" height="220" viewBox="0 0 350 220" aria-hidden="true">
      <path d="M0,10 Q40,0 90,40 L350,40 V220 H0 Z" fill="var(--navy)"/>
      <path d="M0,10 Q40,0 90,40 L350,40" fill="none" stroke="var(--navy-dark)" stroke-width="2"/>
    </svg>
    <div class="card-slot"></div>
  </div>
</section>

</body>
</html>
```